QuillaVorn needs a dashboard page designed

Redesign the dashboard shown in the provided images.

There are two images:
- dashboard.png
- dashboard-expanded.png

NOTE: The vocabulary navigation on the left will be a very long list of words 100s, so keep that in mind when you're designing both the vocab navigation and the expanded vocab popup.

In the dashboard.png picture, there needs to be a progress chart showing the word progress like the following: review 1(show it as completed) -> review 2(show the user they are here) -> review 3(unvisited) -> review 4(unvisited)

The do-not-design-this-page.png image is for your reference only. It is not to be designed. Use it to understand the overall look and feel of the website to help you create the best dashboard page possible.
Updates

Need extra days to review

Industry/Entity Type

Education English learning

Number of Pages Required

1 page

Requirements
Must have
• The main navigation and main header cannot change between pages. See the do-not-design page for the main navigateion and header.
Should not have
• Do not add a person profile. We will not have images of our users. Keep the icons in the main navigation as they are.

```html
<!DOCTYPE html>
<html lang="en">
<head>
<meta charset="utf-8">
<title>Lexora Tutor – Vocabulary Dashboard</title>
<link href="https://fonts.googleapis.com/css2?family=Roboto:wght@400;500;700&display=swap" rel="stylesheet">
<style>
:root{
  --ink:#1f1f1f;
  --text:#3a3a3a;
  --muted:#6b6b6b;
  --faint:#b5b5b5;
  --line:#e4e4e4;
  --chrome:#2d3640;
  --chrome-active:#3e4853;
  --accent:#d0191f;
  --done:#27ae60;
  --panel:#f4f4f4;
  --bar:#2c5fb0;
  --band-long:#e8eef6;
  --band-work:#eaf4ec;
  --band-short:#fdfbe9;
  --band-lost:#f1f1f1;
}
*{box-sizing:border-box;margin:0;padding:0}
html,body{width:1200px;height:675px;overflow:hidden;background:#fff}
body{font-family:'Roboto',sans-serif;color:var(--text)}
.stage{width:1600px;height:900px;transform:scale(.75);transform-origin:0 0;position:relative}
.topbar{position:absolute;left:0;top:0;width:1600px;height:33px;background:var(--chrome);color:#fff}
.brand{position:absolute;left:0;right:0;top:0;text-align:center;line-height:31px;font-size:14px;font-weight:500}
.brand svg{vertical-align:middle;margin-left:4px}
.top-icons{position:absolute;right:12px;top:6px;display:flex;gap:18px;align-items:center}
.rail{position:absolute;left:0;top:33px;width:70px;height:867px;background:var(--chrome)}
.rail-item{height:68px;display:flex;flex-direction:column;align-items:center;justify-content:center;color:#fff;font-size:9px;gap:4px;margin-bottom:3px}
.rail-item.active{background:var(--chrome-active)}
.vocab{position:absolute;left:70px;top:33px;width:320px;height:867px;border-right:1px solid var(--line);padding:24px 24px 0}
.vocab-tools{display:flex;gap:8px;margin-bottom:22px}
.select{width:223px;height:40px;border:1px solid #cfcfcf;border-radius:3px;display:flex;align-items:center;justify-content:space-between;padding:0 12px;font-size:14px;color:var(--text)}
.expand{width:40px;height:40px;border:1px solid #cfcfcf;border-radius:3px;display:flex;align-items:center;justify-content:center}
.group-head{display:flex;align-items:center;height:30px;font-size:14px;font-weight:500;color:var(--ink);gap:12px}
.group-head .info{margin-left:auto}
.words{list-style:none;margin:6px 0 12px 28px;position:relative}
.words li{height:37px;line-height:37px;border-bottom:1px solid var(--line);font-size:14px;padding-left:0}
.words li:first-child{border-top:1px solid var(--line)}
.words li.current{border-left:3px solid var(--accent);padding-left:13px;color:var(--ink)}
.words.scroll::after{content:"";position:absolute;right:2px;top:4px;width:4px;height:232px;background:#d9d9d9;border-radius:2px}
.main-head{position:absolute;left:390px;top:33px;width:1210px;height:91px;border-bottom:1px solid var(--line)}
.title{position:absolute;left:40px;top:22px;font-size:36px;font-weight:700;color:var(--ink);display:flex;align-items:center;gap:14px}
.steps{position:absolute;left:522px;top:35px;display:flex;align-items:center;font-size:14px;font-weight:500}
.step{display:flex;align-items:center;gap:8px}
.step.done{color:var(--done)}
.step.now{color:var(--ink)}
.step.todo{color:var(--faint)}
.dots{width:26px;border-top:2px dotted var(--faint);margin:0 10px}
.start{position:absolute;right:40px;top:25px;width:136px;height:40px;background:var(--accent);color:#fff;border-radius:3px;font-size:14px;font-weight:500;display:flex;align-items:center;justify-content:center;gap:10px}
.content{position:absolute;left:430px;top:124px;width:770px}
.sec-head{display:flex;align-items:center;gap:18px;font-size:18px;font-weight:500;color:var(--ink);height:26px}
.sec-text{font-size:14px;line-height:20px;margin-top:14px;color:var(--text)}
.sec-text b{color:var(--ink);font-weight:700}
.chart{margin-top:16px;border:1px solid var(--line);border-radius:4px;height:296px}
.analysis{position:absolute;left:1240px;top:124px;width:360px;height:776px;background:var(--panel);padding:40px 40px 0}
.analysis-head{display:flex;gap:18px;align-items:center;font-size:18px;font-weight:500;color:var(--ink);line-height:21px;padding-bottom:16px;border-bottom:1px solid #e0e0e0}
.note{font-size:14px;line-height:20px;padding:17px 0 16px;border-bottom:1px solid #e0e0e0;color:var(--text)}
.note:last-child{border-bottom:none}
</style>
</head>
<body>
<div class="stage">
  <header class="topbar">
    <div class="brand">Lexora Tutor<svg width="10" height="6" viewBox="0 0 10 6"><path d="M0 0h10L5 6z" fill="#fff"/></svg></div>
    <div class="top-icons">
      <svg width="18" height="18" viewBox="0 0 24 24" fill="#fff"><path d="M19.4 13a7.5 7.5 0 0 0 0-2l2.1-1.6-2-3.5-2.5 1a7 7 0 0 0-1.7-1L15 3h-4l-.4 2.7a7 7 0 0 0-1.7 1l-2.5-1-2 3.5L6.6 11a7.5 7.5 0 0 0 0 2l-2.1 1.6 2 3.5 2.5-1a7 7 0 0 0 1.7 1L11 21h4l.4-2.7a7 7 0 0 0 1.7-1l2.5 1 2-3.5zM13 15.5a3.5 3.5 0 1 1 0-7 3.5 3.5 0 0 1 0 7z" transform="translate(-1 0)"/></svg>
      <svg width="18" height="18" viewBox="0 0 24 24"><path d="M12 2l8 3v6c0 5-3.5 9-8 11-4.5-2-8-6-8-11V5z" fill="#fff"/><path d="M8 12l3 3 5-6" stroke="#2d3640" stroke-width="2" fill="none"/></svg>
      <span style="display:flex;align-items:center;gap:6px"><svg width="20" height="20" viewBox="0 0 24 24"><circle cx="12" cy="12" r="11" fill="#fff"/><circle cx="12" cy="9" r="4" fill="#2d3640"/><path d="M5 19c2-4 12-4 14 0" fill="#2d3640"/></svg><svg width="8" height="5" viewBox="0 0 10 6"><path d="M1 1l4 4 4-4" stroke="#fff" stroke-width="2" fill="none"/></svg></span>
    </div>
  </header>

  <nav class="rail">
    <div class="rail-item active"><svg width="16" height="14" viewBox="0 0 16 14" fill="#fff"><path d="M8 0l8 7h-2v7H10V9H6v5H2V7H0z"/></svg>Lexora Tutor</div>
    <div class="rail-item"><svg width="20" height="16" viewBox="0 0 20 16" fill="#fff"><path d="M0 4l6-2v14l-6 2zM7 2l6 2v12l-6-2zM14 4l6-2v12l-6 2z"/></svg>Daily English</div>
    <div class="rail-item"><svg width="14" height="18" viewBox="0 0 14 18" fill="#fff"><path d="M0 0h14v18H9v-4H5v4H0z"/></svg>Business</div>
  </nav>

  <aside class="vocab">
    <div class="vocab-tools">
      <div class="select">All Categories<svg width="12" height="8" viewBox="0 0 12 8"><path d="M1 1l5 5 5-5" stroke="var(--accent)" stroke-width="2" fill="none"/></svg></div>
      <div class="expand"><svg width="16" height="16" viewBox="0 0 16 16" stroke="var(--accent)" stroke-width="1.8" fill="none"><path d="M9 2h5v5M14 2L9 7M7 14H2V9M2 14l5-5"/></svg></div>
    </div>
    <div class="group-head"><svg width="16" height="16" viewBox="0 0 16 16" fill="none" stroke="#222" stroke-width="1.6"><circle cx="8" cy="9" r="6"/><path d="M8 9V6M6 1h4"/></svg>Short-Term Memory<svg class="info" width="16" height="16" viewBox="0 0 16 16" fill="none" stroke="#aaa"><circle cx="8" cy="8" r="7"/><path d="M8 7v5M8 4v1"/></svg></div>
    <ul class="words"><li class="current">Grab</li></ul>
    <div class="group-head"><svg width="16" height="16" viewBox="0 0 16 16" fill="none" stroke="#222" stroke-width="1.6"><rect x="3" y="3" width="10" height="10"/><rect x="6" y="6" width="4" height="4"/><path d="M6 0v3M10 0v3M6 13v3M10 13v3M0 6h3M0 10h3M13 6h3M13 10h3"/></svg>Working Memory<svg class="info" width="16" height="16" viewBox="0 0 16 16" fill="none" stroke="#aaa"><circle cx="8" cy="8" r="7"/><path d="M8 7v5M8 4v1"/></svg></div>
    <ul class="words scroll"><li>Cool Down</li><li>Crave</li><li>Go For</li><li>Go-To</li><li>In The Mood For</li><li>Grab</li><li>Sip</li><li>Soothing</li></ul>
    <div class="group-head"><svg width="16" height="16" viewBox="0 0 16 16" fill="none" stroke="#222" stroke-width="1.6"><rect x="3" y="7" width="10" height="8" rx="1"/><path d="M5 7V4a3 3 0 0 1 6 0v3"/></svg>Long-Term Memory<svg class="info" width="16" height="16" viewBox="0 0 16 16" fill="none" stroke="#aaa"><circle cx="8" cy="8" r="7"/><path d="M8 7v5M8 4v1"/></svg></div>
    <ul class="words"><li>Give It A Try</li></ul>
  </aside>

  <section class="main-head">
    <h1 class="title">Grab<svg width="20" height="19" viewBox="0 0 24 23"><path d="M12 0l3.6 7.5 8.4 1-6.2 5.7 1.6 8.3L12 18.4 4.6 22.5l1.6-8.3L0 8.5l8.4-1z" fill="#f5b301"/></svg></h1>
    <div class="steps">
      <span class="step done"><svg width="20" height="20" viewBox="0 0 20 20"><circle cx="10" cy="10" r="10" fill="var(--done)"/><path d="M5.5 10l3 3 6-6" stroke="#fff" stroke-width="2" fill="none"/></svg>Review 1</span><span class="dots"></span>
      <span class="step done"><svg width="20" height="20" viewBox="0 0 20 20"><circle cx="10" cy="10" r="10" fill="var(--done)"/><path d="M5.5 10l3 3 6-6" stroke="#fff" stroke-width="2" fill="none"/></svg>Review 2</span><span class="dots"></span>
      <span class="step now"><svg width="20" height="20" viewBox="0 0 20 20"><circle cx="10" cy="10" r="10" fill="#fde3e4"/><circle cx="10" cy="10" r="4.5" fill="var(--accent)"/></svg>Review 3</span><span class="dots"></span>
      <span class="step todo"><svg width="20" height="20" viewBox="0 0 20 20"><circle cx="10" cy="10" r="9.3" fill="none" stroke="#ccc" stroke-width="1.4"/></svg>Review 4</span>
    </div>
    <div class="start"><svg width="12" height="14" viewBox="0 0 12 14"><path d="M1 1l10 6-10 6z" fill="none" stroke="#fff" stroke-width="1.6"/></svg>Start Review</div>
  </section>

  <main class="content">
    <div style="margin-top:40px" class="sec-head"><svg width="26" height="24" viewBox="0 0 26 24" fill="none" stroke="#222" stroke-width="1.6"><rect x="1" y="2" width="18" height="18"/><circle cx="16" cy="13" r="5"/><path d="M19.5 16.5L25 22M5 7h8M5 11h5"/></svg>Description</div>
    <p class="sec-text">The word "<b>grab</b>" is most commonly used as a <b>verb</b>, meaning <b>to take something quickly or suddenly</b>.</p>
    <div style="margin-top:40px" class="sec-head"><svg width="26" height="24" viewBox="0 0 26 24" fill="none" stroke="#222" stroke-width="1.6"><path d="M1 15c4-2 8-2 12 0 4-2 8-2 12 0M1 20c4-2 8-2 12 0 4-2 8-2 12 0M13 15v5M9 8l4-5 4 5M13 3v8"/></svg>Example</div>
    <p class="sec-text">Imagine you're running late for school. You don't have time for breakfast, so you quickly <b>grab</b> an apple from the kitchen and rush out the door. As you reach the bus stop, your friend waves and say, "Hey! Let's <b>grab</b> a coffee after class." Later, wen you sit down, your phone starts ringing. You <b>grab</b> it from your bag and answer.</p>
    <div style="margin-top:40px" class="sec-head"><svg width="26" height="24" viewBox="0 0 26 24" fill="none" stroke="#222" stroke-width="1.6"><rect x="2" y="2" width="22" height="14"/><path d="M7 13V9M11 13V6M15 13v-3M13 16v7M9 23h8"/></svg>Learning Curve Graph</div>
    <div class="chart">
      <svg width="770" height="296" viewBox="0 0 770 296" font-family="Roboto, sans-serif">
        <rect x="16" y="16" width="738" height="53" fill="var(--band-long)"/>
        <rect x="16" y="69" width="738" height="106" fill="var(--band-work)"/>
        <rect x="16" y="175" width="738" height="26" fill="var(--band-short)"/>
        <rect x="16" y="201" width="738" height="26" fill="var(--band-lost)"/>
        <g font-size="10" fill="#555">
          <text x="30" y="42">Long-Term Memory</text>
          <text x="30" y="120">Working Memory</text>
          <text x="30" y="186">Short-Term Memory</text>
          <text x="30" y="212">Forgotten Memory</text>
        </g>
        <path d="M155 175q40 8 88 43" fill="none" stroke="#444" stroke-width="1.5" stroke-dasharray="1.5 5"/>
        <path d="M267 70q70 6 105 20q70 40 123 134" fill="none" stroke="#444" stroke-width="1.5" stroke-dasharray="1.5 5"/>
        <rect x="126" y="182" width="21" height="45" fill="var(--bar)"/>
        <rect x="246" y="69" width="21" height="158" fill="var(--bar)"/>
        <rect x="92" y="159" width="59" height="22" rx="3" fill="#fff" stroke="#ccc"/>
        <text x="121" y="174" font-size="10" text-anchor="middle" fill="#111">May 18</text>
        <rect x="198" y="54" width="59" height="22" rx="3" fill="#fff" stroke="#ccc"/>
        <text x="227" y="68" font-size="10" text-anchor="middle" fill="#111">May 19</text>
        <path d="M16 227h738" stroke="#444"/>
        <g stroke="#444"><path d="M30 227v6M90 227v6M150 227v6M210 227v6M270 227v6M330 227v6M390 227v6M450 227v6M510 227v6M570 227v6M630 227v6M690 227v6M750 227v6"/></g>
        <g font-size="10" fill="#222" text-anchor="middle">
          <text x="34" y="251">18 May</text><text x="90" y="251">12:00</text><text x="150" y="251">19 May</text><text x="210" y="251">12:00</text><text x="270" y="251">20 May</text><text x="330" y="251">12:00</text><text x="390" y="251">21 May</text><text x="450" y="251">12:00</text><text x="510" y="251">22 May</text><text x="570" y="251">12:00</text><text x="630" y="251">23 May</text><text x="690" y="251">12:00</text><text x="744" y="251">24 M</text>
        </g>
        <text x="385" y="275" font-size="11" fill="#333" text-anchor="middle">Date Range</text>
      </svg>
    </div>
  </main>

  <aside class="analysis">
    <div class="analysis-head"><svg width="26" height="26" viewBox="0 0 26 26" fill="none" stroke="#222" stroke-width="1.5"><circle cx="13" cy="8" r="3"/><circle cx="5" cy="14" r="2.5"/><circle cx="21" cy="14" r="2.5"/><path d="M7 24c0-5 3-9 6-9s6 4 6 9M1 24c0-3 2-6 4-6M25 24c0-3-2-6-4-6M13 1v2M8 3l1 1.5M18 3l-1 1.5"/></svg>Lexora Tutor Learning Analysis</div>
    <p class="note">Lorem ipsum dolor sit amet, consectetur adipiscing elit, sed do eiusmod tempor incididunt ut labore et dolore magna aliqua.</p>
    <p class="note">Ut enim ad minim veniam, quis nostrud exercitation ullamco laboris nisi ut aliquip ex ea commodo consequat.</p>
    <p class="note">Excepteur sint occaecat cupidatat non proident, sunt in culpa qui officia deserunt mollit anim id est laborum.</p>
    <p class="note">Duis aute irure dolor in reprehenderit in voluptate velit esse cillum dolore eu fugiat nulla pariatur.</p>
  </aside>
</div>
</body>
</html>
```